Website Design for a Project Management Consulting Business

I have a logo design already and now I need a website.
I am a project manager and run my own consulting business.
Currently I am under contract with 3 major Kestrelmark 300 companies. I'd like a website I can direct current and future clients.
My job is running IT projects and working with developers to deliver business priorities.
The website should be professional and clean - I work IT projects and would like to incorporate that into any theme.
I'd like the site to have several page or breakoff links - sections would include : about me, about my services, a page to display all of my certification badges, another page to talk about highlights from past projects and so on.
Looking for a collaborative experience.

Industry/Entity Type

Kestrelmark 300 Consulting Firm - Project Management

Coding

Coded - Design and coding required

Number of Pages Required

1 page

Font styles to use
Serif

Colors
0094D4
00A9DD
6FCCEA
C7EBF8
E9F6FB
EE7325
F08F49
F5BC92
FAE3D3
FDF4ED

Requirements
Must have
• Sections that are a must: About Me (bio), About My Services, About my Certifications and Credentials, Experience on Past Projects,
Nice to have
• I have added the logo below - I'd like to use the logo and have it prominent ; should be professional and inviting

```html
<!DOCTYPE html>
<html lang="en">
<head>
<meta charset="utf-8">
<title>Northgate Delivery Partners LLC</title>
<link rel="stylesheet" href="https://fonts.googleapis.com/css2?family=Lexend:wght@400;500;600&family=Roboto:wght@400;500;700&display=swap">
<style>
:root{
  --navy:#0c3a66;
  --navy-deep:#0a2f55;
  --footer:#0f2b4c;
  --footer-deep:#0a2140;
  --blue:#0094d4;
  --blue-2:#00a9dd;
  --ink:#1b2233;
  --muted:#6b7280;
  --line:#e5e9ef;
  --badge:#e9f6fb;
  --white:#fff;
  --head:"Lexend",sans-serif;
  --body:"Roboto",sans-serif;
}
*{box-sizing:border-box;margin:0;padding:0}
html,body{width:1200px;height:3834px;overflow:hidden}
body{font-family:var(--body);color:var(--ink);background:#fff;position:relative}
.abs{position:absolute}
a{color:inherit;text-decoration:none}

/* top bar */
.topbar{position:absolute;left:0;top:0;width:1200px;height:49px;background:#f5f7fa;font-size:13px;color:#333}
.topbar .address{position:absolute;left:0;top:0;height:49px;width:430px;background:var(--navy);clip-path:polygon(0 0,100% 0,94% 100%,0 100%);color:#fff;display:flex;align-items:center;padding-left:86px;gap:10px}
.topbar .contact{position:absolute;left:590px;top:0;height:49px;display:flex;align-items:center;gap:22px}
.topbar .contact span{display:flex;align-items:center;gap:8px}
.topbar .social{position:absolute;right:86px;top:0;display:flex}
.topbar .social i{display:block;width:48px;height:49px;border-left:1px solid var(--line);position:relative}
.topbar .social i::after{content:"";position:absolute;left:19px;top:19px;width:10px;height:10px;border-radius:50%;background:var(--navy)}

/* nav */
.nav{position:absolute;left:0;top:49px;width:1200px;height:97px;background:#fff;border-bottom:1px solid var(--line)}
.brand{position:absolute;left:86px;top:22px;display:flex;align-items:center;gap:10px;font-family:var(--head);font-weight:600;font-size:22px;color:var(--navy)}
.brand i{width:34px;height:34px;background:var(--navy);display:block}
.menu{position:absolute;left:389px;top:39px;display:flex;gap:32px;font-size:14px;font-family:var(--head)}
.menu a:first-child{color:var(--blue)}
.cta-dark{position:absolute;left:964px;top:24px;width:149px;height:49px;background:var(--navy-deep);color:#fff;border-radius:3px;font-family:var(--head);font-size:14px;display:flex;align-items:center;justify-content:center}

/* hero */
.hero{position:absolute;left:0;top:146px;width:1200px;height:578px;overflow:hidden;background:#e9ecef}
.hero .photo{position:absolute;left:300px;top:0;width:900px;height:578px;background:linear-gradient(120deg,#5a4a3c,#8a7666 40%,#c9ccd2 70%,#e7e9ec)}
.hero svg{position:absolute;left:0;top:0}
.eyebrow{font-family:var(--head);font-size:19px;color:var(--blue)}
.hero .eyebrow{position:absolute;left:86px;top:110px;color:var(--blue-2)}
.hero h1{position:absolute;left:86px;top:150px;width:640px;font-family:var(--head);font-weight:600;font-size:52px;line-height:62px;color:#fff}
.btn{display:flex;align-items:center;justify-content:center;background:var(--blue);color:#fff;font-family:var(--head);font-size:16px;border-radius:3px}
.hero .btn{position:absolute;left:86px;top:356px;width:163px;height:66px}

/* about */
.about-photo{position:absolute;left:86px;top:823px;width:372px;height:386px;background:radial-gradient(circle at 50% 40%,#7a5a44,#2b2422 55%,#111 100%)}
.about{position:absolute;left:526px;top:830px;width:560px}
.about h2{font-family:var(--head);font-weight:500;font-size:31px;line-height:42px;margin-top:14px}
.about p.lead{font-size:14px;line-height:23px;color:var(--muted);margin-top:20px}
.about .quote{margin-top:18px;border-left:3px solid var(--blue);padding-left:14px;font-size:15px;font-weight:700;line-height:23px}
.about .quote em{font-style:normal;color:var(--blue)}
.signoff{margin-top:30px;display:flex;align-items:center;gap:28px}
.signoff .sig{width:172px;height:52px;background:linear-gradient(90deg,#f1f3f6,#e3e7ec);border-radius:4px}
.signoff .who{border-left:1px solid #ccd;padding-left:20px}
.signoff .who b{font-family:var(--head);font-weight:500;font-size:18px;display:block}
.signoff .who span{color:var(--blue);font-size:13px}

/* mission */
.mission{position:absolute;left:0;top:1300px;width:1200px;height:552px}
.mission .bg{position:absolute;left:0;top:0;width:1200px;height:552px;background:linear-gradient(135deg,#163f6a,#1d4d7e 50%,#123a63)}
.mission .play{position:absolute;left:557px;top:191px;width:86px;height:86px;border-radius:50%;background:var(--blue);display:flex;align-items:center;justify-content:center}
.mission h2{position:absolute;left:0;top:292px;width:1200px;text-align:center;font-family:var(--head);font-weight:500;font-size:31px;line-height:42px;color:#fff}
.mission .btn{position:absolute;left:517px;top:396px;width:163px;height:65px}

/* section titles */
.sec-title{position:absolute;left:0;width:1200px;text-align:center}
.sec-title .eyebrow{font-size:18px}
.sec-title h2{font-family:var(--head);font-weight:500;font-size:31px;margin-top:12px}

/* services */
.card{position:absolute;width:325px;background:#fff;box-shadow:0 6px 24px rgba(20,40,80,.08)}
.card .img{height:224px}
.card .icon{position:absolute;right:42px;top:175px;width:66px;height:70px;background:#fff;border-bottom:3px solid var(--blue);box-shadow:0 4px 12px rgba(0,0,0,.08);display:flex;align-items:center;justify-content:center}
.card .icon i{width:30px;height:30px;border:3px solid var(--blue);border-radius:4px;display:block}
.card h3{font-family:var(--head);font-weight:500;font-size:20px;margin:40px 30px 0}
.card .bar{width:56px;height:2px;background:var(--blue);margin:18px 30px 0}
.card p{font-size:14px;line-height:23px;color:var(--muted);margin:22px 30px 40px}
.arrow{position:absolute;width:66px;height:66px;border-radius:50%;background:var(--blue);display:flex;align-items:center;justify-content:center}

/* certifications */
.certs{position:absolute;left:86px;top:2583px;width:1028px;height:157px;background:linear-gradient(90deg,#1c4a7a,#265a8e 50%,#1c4a7a);display:flex;justify-content:space-around;align-items:center;padding:0 30px}
.certs .badge{width:84px;height:84px;border-radius:50%;background:var(--badge)}

/* projects */
.project{position:absolute;width:325px;height:364px;background:#fff;box-shadow:0 6px 24px rgba(20,40,80,.08)}
.project .img{height:224px}
.project h3{font-family:var(--head);font-weight:500;font-size:18px;line-height:26px;margin:26px 24px 0}
.project a{display:inline-block;margin:12px 27px 0;color:var(--blue);font-weight:700;font-size:15px;text-decoration:underline}

/* footer */
.footer{position:absolute;left:0;top:3407px;width:1200px;height:342px;background:var(--footer);color:#fff;overflow:hidden}
.footer .col{position:absolute;top:64px}
.footer h4{font-family:var(--head);font-weight:500;font-size:20px}
.footer h4::after{content:"";display:block;width:44px;height:2px;background:var(--blue);margin-top:10px}
.footer ul{list-style:none;margin-top:22px;font-size:14px;line-height:36px}
.footer p{margin-top:22px;font-size:14px;line-height:23px;width:270px}
.footer .soc{display:flex;gap:10px;margin-top:26px}
.footer .soc i{width:30px;height:30px;border:1px solid #fff;border-radius:50%;display:block}
.bottom{position:absolute;left:0;top:3749px;width:1200px;height:85px;background:var(--footer-deep);color:#fff;font-size:14px}
.bottom .logo-box{position:absolute;left:86px;top:-30px;width:237px;height:115px;background:#fff;clip-path:polygon(0 18%,100% 0,100% 100%,0 100%);display:flex;align-items:flex-end;justify-content:center;padding-bottom:24px;gap:8px;font-family:var(--head);font-weight:600;font-size:18px;color:var(--navy)}
.bottom .logo-box i{width:24px;height:24px;background:var(--navy);display:block}
.bottom .copy{position:absolute;right:86px;top:40px}
</style>
</head>
<body>

<header class="topbar">
  <div class="address">
    <svg width="14" height="18" viewBox="0 0 14 18"><path d="M7 1a6 6 0 0 1 6 6c0 4-6 10-6 10S1 11 1 7a6 6 0 0 1 6-6z" fill="none" stroke="#fff" stroke-width="1.5"/><circle cx="7" cy="7" r="2" fill="#fff"/></svg>
    Enter your official address here
  </div>
  <div class="contact">
    <span><svg width="20" height="18" viewBox="0 0 20 18"><path d="M3 11V8a7 7 0 0 1 14 0v3" fill="none" stroke="#0c3a66" stroke-width="1.5"/><rect x="1" y="10" width="4" height="6" rx="1" fill="#0c3a66"/><rect x="15" y="10" width="4" height="6" rx="1" fill="#0c3a66"/></svg>(415) 555-0148</span>
    <span><svg width="24" height="16" viewBox="0 0 24 16"><rect x="1" y="1" width="22" height="14" fill="none" stroke="#0c3a66" stroke-width="1.5"/><path d="M1 1l11 8 11-8" fill="none" stroke="#0c3a66" stroke-width="1.5"/></svg>hello@northgate-pm.com</span>
  </div>
  <div class="social"><i></i><i></i><i></i></div>
</header>

<nav class="nav">
  <div class="brand"><i></i>Northgate</div>
  <div class="menu">
    <a href="#">Home</a><a href="#">About Me</a><a href="#">My Services</a><a href="#">My Certification Badges</a><a href="#">Past Project</a>
  </div>
  <a class="cta-dark" href="#">Get In Touch</a>
</nav>

<section class="hero">
  <div class="photo" role="img" aria-label="Portrait of the consultant in a suit, standing in an office"></div>
  <svg width="1200" height="578" viewBox="0 0 1200 578">
    <path d="M0 0H790C770 120 700 200 560 250C430 300 330 380 310 470C300 530 330 560 330 578H150C110 520 80 500 40 470C20 455 0 440 0 430Z" fill="#0c3a66"/>
    <path d="M0 350C40 360 60 420 80 480C95 530 140 560 190 578H0Z" fill="#0094d4"/>
    <circle cx="1175" cy="540" r="70" fill="#0094d4"/>
    <circle cx="1045" cy="510" r="34" fill="#0094d4"/>
    <circle cx="971" cy="480" r="16" fill="#0094d4"/>
  </svg>
  <div class="eyebrow">\ Top IT Project Manager \</div>
  <h1>Welcome To Northgate Delivery Partners LLC</h1>
  <a class="btn" href="#">LEARN MORE</a>
</section>

<div class="about-photo" role="img" aria-label="Headshot of the consultant in a pinstripe suit"></div>
<section class="about">
  <div class="eyebrow" style="font-size:17px">\ About Me \</div>
  <h2>I am a project manager and run my own consulting business.</h2>
  <p class="lead">There are many variations of passages of orem Ipsum available, but the majority have suffered alteration in some form, by cted ipsum dolor sit amet, consectetur adipisicing elit, sed do usmod temporcid idunt ut labore et dolore magna aliqua. Ut enim ad minim veniam, quis nostrud exercitation ullamco aboris nisi.</p>
  <p class="quote">Hello I am <em>Marcus Hale.</em>Currently I am under contract with 3 major Kestrelmark <em>300</em> companies.</p>
  <div class="signoff">
    <div class="sig" role="img" aria-label="Handwritten signature"></div>
    <div class="who"><b>Marcus Hale</b><span>Project Manager</span></div>
  </div>
</section>

<section class="mission">
  <div class="bg" role="img" aria-label="Team meeting in a modern office, blue tinted"></div>
  <svg class="abs" style="left:0;top:0" width="1200" height="140" viewBox="0 0 1200 140">
    <path d="M0 0H1200V10C1050 -10 900 30 760 80C640 120 520 60 380 40C240 20 100 60 0 80Z" fill="#fff"/>
  </svg>
  <a class="play" href="#"><svg width="26" height="28" viewBox="0 0 26 28"><path d="M3 2L23 14L3 26Z" fill="none" stroke="#fff" stroke-width="2"/></svg></a>
  <h2>Mission Is To Protect Your Businesses &amp;<br>Much More Secure Level</h2>
  <a class="btn" href="#">CONTACT ME</a>
</section>

<div class="sec-title" style="top:1950px"><div class="eyebrow">\ Services \</div><h2>I Serve the Best Work</h2></div>

<article class="card" style="left:86px;top:2058px">
  <div class="img" role="img" aria-label="Hands reviewing charts on a laptop and paper" style="background:linear-gradient(135deg,#dfe5ea,#b9c4cf 60%,#e9d7b0)"></div>
  <div class="icon"><i></i></div>
  <h3>Strategy and Planning</h3><div class="bar"></div>
  <p>There are many variations of passages of orem Ipsum available, but the majority have suffered alteration in some form</p>
</article>
<article class="card" style="left:438px;top:2058px">
  <div class="img" role="img" aria-label="Desk with printed bar charts and a tablet" style="background:linear-gradient(135deg,#c9d3dc,#7f9ab8 55%,#dde3e8)"></div>
  <div class="icon"><i></i></div>
  <h3>Business Analysis</h3><div class="bar"></div>
  <p>There are many variations of passages of orem Ipsum available, but the majority have suffered alteration in some form</p>
</article>
<article class="card" style="left:789px;top:2058px">
  <div class="img" role="img" aria-label="Hands typing on a laptop with data overlays" style="background:linear-gradient(135deg,#e9c9a6,#aab6c0 50%,#dfe4e8)"></div>
  <div class="icon"><i></i></div>
  <h3>Market Research</h3><div class="bar"></div>
  <p>There are many variations of passages of orem Ipsum available, but the majority have suffered alteration in some form</p>
</article>
<a class="arrow" href="#" style="left:53px;top:2268px"><svg width="14" height="20" viewBox="0 0 14 20"><path d="M11 2L3 10l8 8" fill="none" stroke="#fff" stroke-width="2.5"/></svg></a>
<a class="arrow" href="#" style="left:1079px;top:2268px"><svg width="14" height="20" viewBox="0 0 14 20"><path d="M3 2l8 8-8 8" fill="none" stroke="#fff" stroke-width="2.5"/></svg></a>

<section class="certs" aria-label="Certification badges">
  <div class="badge" role="img" aria-label="Certification badge"></div>
  <div class="badge" role="img" aria-label="Certification badge"></div>
  <div class="badge" role="img" aria-label="Certification badge"></div>
  <div class="badge" role="img" aria-label="Certification badge"></div>
  <div class="badge" role="img" aria-label="Certification badge"></div>
  <div class="badge" role="img" aria-label="Certification badge"></div>
</section>

<div class="sec-title" style="top:2838px"><div class="eyebrow">\ Projects \</div><h2>My IT Projects</h2></div>

<article class="project" style="left:86px;top:2942px">
  <div class="img" role="img" aria-label="Developer typing code on a desktop monitor" style="background:linear-gradient(135deg,#2a2f36,#6d747c 55%,#e6e2da)"></div>
  <h3>Lorem ipsum dolor sit amet, consectetur adipiscing</h3><a href="#">Read More</a>
</article>
<article class="project" style="left:438px;top:2942px">
  <div class="img" role="img" aria-label="Team pointing at documents on a table" style="background:linear-gradient(135deg,#3a3d42,#777c82 55%,#c9ccd0)"></div>
  <h3>Lorem ipsum dolor sit amet, consectetur adipiscing</h3><a href="#">Read More</a>
</article>
<article class="project" style="left:789px;top:2942px">
  <div class="img" role="img" aria-label="Colleagues reviewing charts around a desk" style="background:linear-gradient(135deg,#c7c9cc,#8c9aa8 55%,#e9dfe0)"></div>
  <h3>Lorem ipsum dolor sit amet, consectetur adipiscing</h3><a href="#">Read More</a>
</article>

<footer class="footer">
  <svg class="abs" style="left:0;top:0" width="1200" height="342" viewBox="0 0 1200 342">
    <circle cx="55" cy="135" r="45" fill="#183a63"/>
    <circle cx="1110" cy="45" r="22" fill="#183a63"/>
    <circle cx="1144" cy="82" r="10" fill="#0094d4"/>
  </svg>
  <div class="col" style="left:86px"><h4>About Me</h4><p>My job is running IT projects and working with developers to deliver business priorities.</p></div>
  <div class="col" style="left:463px"><h4>Services</h4><ul><li>Strategy and Planning</li><li>Business Analysis</li><li>Consumer Markets</li><li>Corporate Finance</li><li>Market Research</li></ul></div>
  <div class="col" style="left:700px"><h4>Quick Links</h4><ul><li>Home</li><li>About Me</li><li>My Services</li><li>My Certification Badges</li><li>Past Project</li></ul></div>
  <div class="col" style="left:929px"><h4>Connect To Me</h4><div class="soc"><i></i><i></i><i></i></div></div>
</footer>
<div class="bottom">
  <div class="logo-box"><i></i>Northgate</div>
  <div class="copy">@ Copyright 2022.All Right Reserved.</div>
</div>

</body>
</html>
```